Sales Flyer offering home being built and items included as well as options

We are custom home builders and we need a flyer to place in literature boxes on lots where we are building a house. Most times it's a lot and home package. But sometimes it's just a home to be built on someone lot they already own. We'd like it to list items that are included and the options being offered. It will have to have our business contact info., website info, etc.
We'd like it to have colors to go with our website and logo.
www.fendrickandloame.com. You may use some of the wording from our website if needed. We want a place to upload the house that we intend to build, which will change, (not all projects are the same house) plus maybe side stock pictures of our homes or things inside the home we have built.
This file would have to be so that it will allow us to change the sales price, items included and options from time to time and anything else that needs to changed, depending upon where we are building. I will upload an example of one we have used in the past that I did myself. But I know it can be done better

Target Market(s)

People looking for new custom home to be constructed. Usually people driving by.

Industry/Entity Type

Building

Colors

Designer to choose colors to be used in the design.

Requirements
Must have
• This is a sales flyer. Need to be professional and eye catchy, but yet elegant, pleasing to the eye.
• Our company information (see website) or current flyer uploaded.
• Website info.
• Logo (see website)
• Facebook info
• Need to be able to make changes to flyer. Can not be in just PDF
• Need to be able to print in our office, since each project changes.
• Picture of house being built, picture on flyer uploaded is the current home being offered. Must have items included and options being offered
Nice to have
• Stock pictures. Colors to go with website and logo.

```html
<!DOCTYPE html>
<html lang="en">
<head>
<meta charset="utf-8">
<title>Fendrick and Loame Custom Homes – Lot and Home Package</title>
<link href="https://fonts.googleapis.com/css2?family=Lato:ital,wght@0,400;0,700;1,400&family=Cinzel:wght@400;700&display=swap" rel="stylesheet">
<style>
  :root{
    --gold:#c18f2c;
    --gold-dark:#a97a1f;
    --charcoal:#272727;
    --ink:#1c1c1c;
    --grey-band:#e6e6e6;
    --grey-text:#555;
    --white:#ffffff;
    --sky:#7f9dc4;
    --lawn:#5d8a3a;
  }
  *{box-sizing:border-box;margin:0;padding:0}
  html,body{width:931px;height:1200px;overflow:hidden;background:var(--white)}
  body{font-family:'Lato',sans-serif;color:var(--ink);position:relative}
  .flyer{position:absolute;left:90px;top:115px;width:751px;height:971px}
  .hero-photo{position:absolute;left:0;top:0;width:751px;height:334px;
    background:linear-gradient(180deg,var(--sky) 0%,#b9c9de 40%,#b45a2f 62%,#8a4a2a 75%,var(--lawn) 86%,#4a7030 100%)}
  .brand-panel{position:absolute;left:0;top:338px;width:321px;height:346px;background:var(--charcoal);color:var(--white);text-align:center}
  .brand-mark{position:absolute;left:146px;top:60px;width:30px;height:30px;background:var(--gold)}
  .brand-name{position:absolute;left:0;width:100%;top:150px;font-family:'Cinzel',serif;font-size:20px;color:var(--gold);letter-spacing:1px}
  .brand-sub{position:absolute;left:0;width:100%;top:174px;font-family:'Cinzel',serif;font-size:11px;color:var(--gold);letter-spacing:4px}
  .brand-tag{position:absolute;left:0;width:100%;top:187px;font-size:9px;color:var(--gold)}
  .package-title{position:absolute;left:0;width:100%;top:232px;font-family:'Cinzel',serif;font-weight:700;font-size:29px;line-height:34px;letter-spacing:1px}
  .feature-panel{position:absolute;left:321px;top:338px;width:430px;height:346px;background:linear-gradient(135deg,var(--gold-dark),var(--gold) 50%,var(--gold-dark))}
  .checklist{position:absolute;list-style:none}
  .checklist li{position:relative;padding-left:19px;font-size:11.5px;line-height:13px;margin-bottom:7px;color:var(--ink)}
  .checklist li svg{position:absolute;left:0;top:0;width:12px;height:12px}
  .included.col-a{left:42px;top:32px}
  .included.col-b{left:221px;top:32px}
  .included.col-b li{margin-bottom:8.4px}
  .options-title{position:absolute;left:0;width:100%;top:204px;text-align:center;font-size:12.5px;font-weight:700}
  .options.col-a{left:42px;top:224px}
  .options.col-b{left:221px;top:224px}
  .options li{text-transform:uppercase;font-size:11px}
  .sale-price{position:absolute;left:37px;top:317px;font-size:19px;font-weight:700}
  .hoa-note{position:absolute;left:244px;top:321px;font-size:13px;font-style:italic}
  .promises{position:absolute;left:0;top:684px;width:751px;height:116px;display:flex}
  .promise{flex:1;text-align:center;font-size:10.5px;line-height:14px;color:var(--grey-text);padding-top:14px;border-right:1px solid #ddd}
  .promise:last-child{border-right:none}
  .promise svg{width:34px;height:34px;display:block;margin:0 auto 10px}
  .contact-band{position:absolute;left:0;top:800px;width:751px;height:120px;background:var(--grey-band)}
  .contact-title{position:absolute;left:0;width:100%;top:11px;text-align:center;color:var(--gold);font-weight:700;font-size:16.5px}
  .contact-motto{position:absolute;left:0;width:100%;top:32px;text-align:center;font-size:16px;color:#333}
  .office-hours{position:absolute;left:44px;top:64px;font-size:12px;line-height:14px}
  .office-hours strong{font-size:13px;display:block}
  .call-line{position:absolute;left:402px;top:68px;font-size:13px;font-weight:700}
  .video-line{position:absolute;left:402px;top:91px;font-size:13px;font-weight:700}
  .footer-bar{position:absolute;left:0;top:920px;width:751px;height:51px;background:var(--charcoal);color:var(--white);font-size:11.5px}
  .footer-bar .accent{position:absolute;right:0;top:0;width:280px;height:39px}
  .footer-item{position:absolute;top:13px;display:flex;align-items:center;gap:6px}
  .footer-item svg{width:13px;height:13px}
  .web{color:var(--charcoal);letter-spacing:.5px}
</style>
</head>
<body>
<main class="flyer">
  <div class="hero-photo" role="img" aria-label="Photo of the featured single-storey home with tan and rust siding, attached garage, lawn and blue sky"></div>

  <section class="brand-panel">
    <div class="brand-mark"></div>
    <div class="brand-name">FENDRICK AND LOAME</div>
    <div class="brand-sub">CUSTOM HOMES</div>
    <div class="brand-tag">Building Homes, Building Relationships</div>
    <h1 class="package-title">IN THIS &nbsp;LOT AND<br>HOME PACKAGE</h1>
  </section>

  <section class="feature-panel">
    <svg width="0" height="0" style="position:absolute">
      <symbol id="tick" viewBox="0 0 12 12"><rect x="1" y="2" width="9" height="9" rx="1.5" fill="none" stroke="#fff" stroke-width="1.3"/><path d="M3.5 6.2l2 2 5.5-6.5" fill="none" stroke="#fff" stroke-width="1.5"/></symbol>
    </svg>
    <ul class="checklist included col-a">
      <li><svg><use href="#tick"/></svg>3 Bedroom</li>
      <li><svg><use href="#tick"/></svg>2 Full Baths</li>
      <li><svg><use href="#tick"/></svg>Custom Tile Shower<br>w/glass enclosure</li>
      <li><svg><use href="#tick"/></svg>Gourmet Kitchen</li>
      <li><svg><use href="#tick"/></svg>Granite Counter Top</li>
      <li><svg><use href="#tick"/></svg>Stainless Steel Appliances</li>
      <li><svg><use href="#tick"/></svg>Hardwood and tile floors</li>
      <li><svg><use href="#tick"/></svg>Carpet in Bedrooms</li>
    </ul>
    <ul class="checklist included col-b">
      <li><svg><use href="#tick"/></svg>9’ Ceilings</li>
      <li><svg><use href="#tick"/></svg>36” Propane Fireplace</li>
      <li><svg><use href="#tick"/></svg>Custom Trim Pkg.</li>
      <li><svg><use href="#tick"/></svg>Crown molding included</li>
      <li><svg><use href="#tick"/></svg>Custom Painting</li>
      <li><svg><use href="#tick"/></svg>Septic &amp; Well</li>
      <li><svg><use href="#tick"/></svg>Asphalt driveway</li>
      <li><svg><use href="#tick"/></svg>Veyra Tankless Water Heater</li>
    </ul>
    <div class="options-title">OPTIONS AVAILABLE</div>
    <ul class="checklist options col-a">
      <li><svg><use href="#tick"/></svg>Soaker Tub</li>
      <li><svg><use href="#tick"/></svg>4 Season Sunroom</li>
      <li><svg><use href="#tick"/></svg>Landscape Pkg</li>
      <li><svg><use href="#tick"/></svg>Irrigation System</li>
    </ul>
    <ul class="checklist options col-b">
      <li><svg><use href="#tick"/></svg>Screened Porch</li>
      <li><svg><use href="#tick"/></svg>Outdoor Shower</li>
      <li><svg><use href="#tick"/></svg>Bonus Room</li>
      <li><svg><use href="#tick"/></svg>Deck</li>
    </ul>
    <div class="sale-price">SALE PRICE &nbsp;$318,500</div>
    <div class="hoa-note">*Hoa Only $285 Per Year</div>
  </section>

  <section class="promises">
    <div class="promise">
      <svg viewBox="0 0 34 34"><rect x="3" y="6" width="28" height="22" fill="none" stroke="#c18f2c" stroke-width="2.5"/><path d="M11 20l6-6 6 6M13 19v6h8v-6" fill="none" stroke="#c18f2c" stroke-width="2"/></svg>
      YOUR DESIGN OR OURS!<br>WE WILL DEISGN AND BUILD<br>YOUR DREAM HOME!
    </div>
    <div class="promise">
      <svg viewBox="0 0 34 34"><rect x="4" y="6" width="12" height="24" fill="none" stroke="#c18f2c" stroke-width="2"/><rect x="18" y="13" width="12" height="17" fill="none" stroke="#c18f2c" stroke-width="2"/><path d="M8 11h4M8 16h4M8 21h4M22 18h4M22 23h4" stroke="#c18f2c" stroke-width="2"/></svg>
      BRING YOUR DESIGN, WE WILL BUILD IT<br>BUILDING HOMES<br>BUILDING RELATIONSHIPS
    </div>
    <div class="promise">
      <svg viewBox="0 0 34 34"><circle cx="17" cy="9" r="5" fill="#c18f2c"/><circle cx="7" cy="13" r="4" fill="#c18f2c"/><circle cx="27" cy="13" r="4" fill="#c18f2c"/><path d="M9 30c0-8 16-8 16 0zM1 30c0-7 10-7 10-2v2zM33 30c0-7-10-7-10-2v2z" fill="#c18f2c"/></svg>
      OUR TEAM KNOWS THAT<br>TRUE SUCCESS IS GROUNDED IN THE<br>RELATIONSHIPS YOU CREATE.
    </div>
  </section>

  <section class="contact-band">
    <div class="contact-title">FENDRICK AND LOAME CUSTOM HOMES</div>
    <div class="contact-motto">Building homes &nbsp;●&nbsp; Building relationships &nbsp;●&nbsp; Brokers Invited</div>
    <div class="office-hours"><strong>OFFICE HOURS</strong>9A.M. - 4 PM. Monday - Friday<br>BY APPOINTMENT (Sat. &amp; Sun.)</div>
    <div class="call-line">CALL US ANYTIME &nbsp;<svg width="12" height="12" viewBox="0 0 12 12"><path d="M3 1l2 2.5-1 1.5c.8 1.5 1.5 2.2 3 3l1.5-1L11 9l-1.5 2C5 10.5 1.5 7 1 2.5z" fill="none" stroke="#c18f2c" stroke-width="1.2"/></svg> 302-555-0148</div>
    <div class="video-line">Check out our video - &nbsp;www.fendrickandloame.com/tour</div>
  </section>

  <footer class="footer-bar">
    <svg class="accent" viewBox="0 0 280 39" preserveAspectRatio="none"><polygon points="0,0 280,0 280,39 40,39" fill="#c18f2c"/></svg>
    <div class="footer-item" style="left:44px"><svg viewBox="0 0 12 12"><path d="M6 11S2 6.5 2 4.5a4 4 0 018 0C10 6.5 6 11 6 11z" fill="none" stroke="#c18f2c" stroke-width="1.4"/><circle cx="6" cy="4.5" r="1.3" fill="#c18f2c"/></svg>1180 Marren Rd Harlow, DE 19950</div>
    <div class="footer-item" style="left:279px"><svg viewBox="0 0 12 12"><rect x="1" y="2.5" width="10" height="7" fill="none" stroke="#c18f2c" stroke-width="1.2"/><path d="M1 2.5l5 4 5-4" fill="none" stroke="#c18f2c" stroke-width="1.2"/></svg>fendrickloame@mail.com</div>
    <div class="footer-item web" style="left:531px"><svg viewBox="0 0 12 12"><circle cx="6" cy="6" r="5" fill="none" stroke="#272727" stroke-width="1.1"/><path d="M1 6h10M6 1c-2.5 3-2.5 7 0 10M6 1c2.5 3 2.5 7 0 10" fill="none" stroke="#272727" stroke-width="1"/></svg>www.fendrickandloame.com</div>
  </footer>
</main>
</body>
</html>
```